Verpackungen für Temperatur-Kalibrierprodukte
Zielgruppe
Wir sind eine Firma, die Temperatur-Kalibrierprodukte vertreibt und suchen ein hochwertiges Design für die Verpackung unserer High-End Thermometer. Unsere Zielgruppe sind Firmen aus Industrie, Forschung und Entwicklung.
Aufgabenstellung
Wir suchen ein Design für eine Magnetbox, in der unsere hochwertigen Thermometer transportiert und aufbewahrt werden. Das Design soll sich an unsere Website-Gestaltung anlehnen, bzw. dazu passen.
Auf die Verpackung sollte das Logo, sowie das Wort 'Präzisionsthermometer'.
Innenmaße der Verpackung:
60 x 13 x 4,5 / 4,5 cm (Breite x Tiefe x Höhe/Klappenhöhe)
Material: 1,8 mm Graubpappe innen weiß
Bezugsmaterial: außen weißes Kraftpapier 157g
Bei Bedarf können wir weiteres Bildmaterial zur Verfügung stellen (siehe Website).

```html
<!DOCTYPE html>
<html lang="de">
<head>
<meta charset="utf-8">
<title>Kalvero Präzisionsthermometer – Magnetbox Deckel</title>
<link rel="stylesheet" href="https://fonts.googleapis.com/css2?family=Roboto:wght@900&display=swap">
<style>
  :root {
    --bg: #f2dbc0;
    --lid-white: #ffffff;
    --lid-edge: #e6e6e6;
    --grey-light: #d3d4cf;
    --grey-mid: #b6b6b0;
    --brand-red: #8e0c1c;
    --ink: #111111;
  }
  html, body {
    margin: 0;
    padding: 0;
    width: 1200px;
    height: 1200px;
    overflow: hidden;
    background: var(--bg);
  }
  .canvas {
    position: relative;
    width: 1200px;
    height: 1200px;
  }
  .lid {
    position: absolute;
    left: 50px;
    top: 480px;
    width: 1100px;
    height: 240px;
    background: var(--lid-white);
    box-shadow: 0 0 0 1px var(--lid-edge);
    overflow: hidden;
  }
  .lid-artwork {
    position: absolute;
    top: 0;
    right: 0;
    width: 330px;
    height: 240px;
    background: linear-gradient(100deg, var(--grey-light) 0%, var(--grey-mid) 45%, var(--brand-red) 100%);
  }
  .brand {
    position: absolute;
    left: 190px;
    top: 44px;
    display: flex;
    align-items: center;
    gap: 14px;
  }
  .brand-dot {
    width: 44px;
    height: 44px;
    border-radius: 50%;
    background: var(--ink);
  }
  .brand-name {
    font-family: "Roboto", Arial, sans-serif;
    font-weight: 900;
    font-size: 56px;
    letter-spacing: 2px;
    color: var(--ink);
    line-height: 1;
  }
  .product-name {
    position: absolute;
    left: 190px;
    top: 118px;
    margin: 0;
    font-family: "Roboto", Arial, sans-serif;
    font-weight: 900;
    font-size: 44px;
    color: var(--ink);
    line-height: 1;
    white-space: nowrap;
  }
  .product-rule {
    position: absolute;
    left: 180px;
    top: 174px;
    width: 250px;
    height: 3px;
    background: var(--brand-red);
  }
</style>
</head>
<body>
  <div class="canvas">
    <section class="lid">
      <div class="lid-artwork" role="img" aria-label="Dekorative Wellengrafik in Grau und Rot"></div>
      <div class="brand">
        <span class="brand-dot"></span>
        <span class="brand-name">Kalvero</span>
      </div>
      <h1 class="product-name">Präzisionsthermometer</h1>
      <div class="product-rule"></div>
    </section>
  </div>
</body>
</html>
```